IT Distribution Wholesale Business Card & Logo Design

I need both logo and a business card that suits our business model, am happy to pay more for great effort put in.
Norvane Bridge Australia Pty Ltd
An IT Distribution / Wholesale company that distributes technology hardwares, softwares, components, etc.
Offer drop ship services for online retailers and supply to Australia-wide.
Based in Sydney Australia.
Design should give impressions of trust and stability.

Slogan: "your one stop technology supplier"
*two-sided name card
*logo + slogan on the back of the card

I don't have much specific requirements, leave it to designers to come up with creative & interesting masterpiece.
The logo and business card comes in first which i would like it to be completed latest by mid of March, we will require a whole redesign of our web pages, banner design, catalogue design later part.

Goodluck & thank you for your effort.

Hello designers,

Busy week, very good return rate on the number of designs and effort put into our business card design.
I thank you all for that.
We will have to extend this project for another week to two to receive more designs and more time for me to post some updates to you all.
We are getting there, i really liked some of the designs sent but just not the perfect masterpiece we are looking for.

Cheers,
Darren P.

Reason: Not getting the perfect piece yet, would like to have more time for designers to give their best shot. Cheers, Darren P.

Target Market(s)

Computer Retailers, Corporate, Schools, Councils.

Industry/Entity Type

Business

Requirements
Must have
• Norvane Bridge (Australia) Pty Ltd, Darren Pell, Managing Director, Unit A, 14-18 Balfour Road, Wexley NSW 2139, Ph +61 2 9371 0422, M +61 4 73925516, E darren@norvanebridge.com.au, W www.norvanebridge.com.au
Nice to have
• Keep it simple & comfortable.
Target audiences are mostly >30-40 years old range.

Example of companies in the same line:-
http://www.qrl.com.au
http://www.zepron.com.au/
http://www.supplyharbourline.com/
http://www.brintel.com.au/
http://www.fwp456.com.au/
https://www.quickdepotweb.com.au/
http://palbreck.com.au/

```html
<!DOCTYPE html>
<html lang="en">
<head>
<meta charset="utf-8">
<title>Norvane Bridge Australia – Business Card</title>
<link rel="stylesheet" href="https://fonts.googleapis.com/css2?family=Open+Sans:wght@300;400;600&family=Arimo:wght@400&display=swap">
<style>
  :root {
    --page-bg: #ecebe9;
    --card-bg: #ffffff;
    --magenta: #a3195b;
    --magenta-deep: #8a1750;
    --ink: #222222;
    --ink-soft: #3c3c3c;
    --grey: #6f6f6f;
    --card-shadow: 0 6px 22px rgba(0,0,0,.14);
  }
  * { box-sizing: border-box; margin: 0; padding: 0; }
  html, body {
    width: 1200px; height: 900px; overflow: hidden;
    background: var(--page-bg);
  }
  .canvas {
    position: relative; width: 1200px; height: 900px;
  }
  .card {
    position: absolute; left: 320px; width: 560px; height: 320px;
    background: var(--card-bg); box-shadow: var(--card-shadow);
  }
  .card--back { top: 70px; }
  .card--front { top: 450px; }

  /* Back: brand + slogan */
  .brand {
    position: absolute; left: 0; right: 0; top: 96px;
    display: flex; align-items: center; justify-content: center; gap: 14px;
  }
  .brand__dot {
    width: 34px; height: 34px; border-radius: 50%; background: var(--magenta);
  }
  .brand__name {
    font-family: "Open Sans", sans-serif; font-weight: 300;
    font-size: 38px; color: var(--ink-soft); letter-spacing: .2px;
  }
  .brand__rule {
    position: absolute; left: 150px; width: 270px; top: 176px;
    height: 2px; background: var(--magenta);
  }
  .brand__slogan {
    position: absolute; left: 0; right: 0; top: 184px; text-align: center;
    font-family: "Open Sans", sans-serif; font-weight: 300;
    font-size: 15px; color: var(--grey); letter-spacing: .4px;
  }

  /* Front: company details */
  .company {
    position: absolute; left: 42px; top: 58px;
    font-family: "Open Sans", sans-serif; font-weight: 300;
    font-size: 15px; color: var(--ink);
  }
  .contact-list { position: absolute; left: 42px; top: 112px; list-style: none; }
  .contact-item {
    display: flex; align-items: flex-start; gap: 12px; margin-bottom: 16px;
    font-family: "Arimo", sans-serif; font-size: 13px; line-height: 15px; color: var(--ink);
  }
  .contact-item svg { flex: none; margin-top: 6px; }
  .divider {
    position: absolute; left: 330px; top: 40px; width: 2px; height: 240px;
    background: var(--magenta);
  }
  .person {
    position: absolute; left: 356px; top: 128px;
    display: flex; align-items: center; gap: 10px;
  }
  .person__badge {
    width: 34px; height: 34px; border-radius: 50%;
    border: 2px solid var(--ink-soft);
  }
  .person__text {
    font-family: "Open Sans", sans-serif; font-weight: 600;
    font-size: 16px; line-height: 18px; color: var(--ink);
  }
</style>
</head>
<body>
<main class="canvas">
  <section class="card card--back">
    <div class="brand">
      <span class="brand__dot"></span>
      <span class="brand__name">Norvane Bridge Australia</span>
    </div>
    <div class="brand__rule"></div>
    <p class="brand__slogan">your one stop technology supplier</p>
  </section>

  <section class="card card--front">
    <p class="company">Norvane Bridge (Australia) Pty Ltd</p>
    <ul class="contact-list">
      <li class="contact-item">
        <svg width="20" height="18" viewBox="0 0 20 18"><polygon points="5,0 15,0 20,9 15,18 5,18 0,9" fill="var(--magenta)"/></svg>
        <span>Unit A, 14-18 Balfour Road<br>Wexley NSW 2139</span>
      </li>
      <li class="contact-item">
        <svg width="20" height="18" viewBox="0 0 20 18"><polygon points="5,0 15,0 20,9 15,18 5,18 0,9" fill="var(--magenta)"/></svg>
        <span>Ph +61 2 9371 0422<br>M +61 4 73925516</span>
      </li>
      <li class="contact-item">
        <svg width="20" height="18" viewBox="0 0 20 18"><polygon points="5,0 15,0 20,9 15,18 5,18 0,9" fill="var(--magenta)"/></svg>
        <span>E darren@norvanebridge.com.au<br>www.norvanebridge.com.au</span>
      </li>
    </ul>
    <div class="divider"></div>
    <div class="person">
      <span class="person__badge"></span>
      <p class="person__text">Darren Pell<br>Managing Director</p>
    </div>
  </section>
</main>
</body>
</html>
```